50c wing mondays

We need a sign reading the following.

HEADING: (large font as the focus of the sign)

50c wing Mondays
from 6pm till late

Medium font under the picture

YOUR CHOICE
- spiced buffalo wings
- hickory smoked BBQ
- Peri Peri

Small font
conditions apply
- minimum 4 wings per serving (of the same type)
- dine in only
- no discount apply

age 18 - 35

50c wing Mondays

Character Logo
• chalkduster

000000
f37122
ffffff

• Our logo
• A picture of wings
• FONT: chalkduster
• Background: BLACK
• Font colour: ORANGE
• Logo: Attached cinder kettle logo
• every word ive stated in the project description
• HEADING MUST BE LARGE: 50c Extra large - - - WING MONDAYS: LARGE
• The rest of the working small
• clip art - too many colours

```html
<!DOCTYPE html>
<html lang="en">
<head>
<meta charset="utf-8">
<title>50¢ Wing Mondays</title>
<link href="https://fonts.googleapis.com/css2?family=Bebas+Neue&family=Graduate&family=Lobster&family=Montserrat:wght@700&display=swap" rel="stylesheet">
<style>
  :root {
    --paper: #ffffff;
    --poster-red: #b04245;
    --teal: #2f5f6c;
    --cream: #f2f1dc;
    --butter: #e9dfa3;
  }
  * { margin: 0; padding: 0; box-sizing: border-box; }
  html, body { width: 844px; height: 1200px; overflow: hidden; background: var(--paper); }
  .poster { position: relative; width: 844px; height: 1200px; background: var(--paper); }
  .poster-field {
    position: absolute; left: 13px; top: 16px; width: 819px; height: 1168px;
    background: var(--poster-red);
  }
  .price {
    position: absolute; left: 0; width: 844px; top: 62px; text-align: center;
    font-family: "Lobster", cursive; font-size: 128px; line-height: 1;
    color: var(--cream); text-shadow: 4px 4px 0 var(--teal);
    transform: skewX(-8deg);
  }
  .headline {
    position: absolute; left: 0; width: 844px; text-align: center;
    font-family: "Bebas Neue", sans-serif; font-size: 178px; line-height: 1;
    color: var(--cream); text-shadow: -6px 6px 0 var(--teal);
  }
  .headline-wing { top: 200px; }
  .headline-mondays { top: 340px; }
  .hours {
    position: absolute; left: 0; width: 844px; top: 508px; text-align: center;
    font-family: "Graduate", serif; font-size: 26px; letter-spacing: 3px;
    color: var(--butter);
  }
  .wings-illustration {
    position: absolute; left: 200px; top: 580px; width: 422px; height: 256px;
    background: var(--butter); border-radius: 45% 45% 50% 50% / 40% 40% 60% 60%;
  }
  .choice-ribbon { position: absolute; left: 130px; top: 830px; width: 580px; height: 100px; }
  .choice-label {
    position: absolute; left: 184px; top: 846px; width: 471px; text-align: center;
    font-family: "Graduate", serif; font-size: 34px; letter-spacing: 3px;
    color: var(--butter);
  }
  .flavours {
    position: absolute; left: 0; width: 844px; top: 898px; text-align: center;
    list-style: none; font-family: "Bebas Neue", sans-serif; font-size: 50px;
    line-height: 50px; color: var(--cream);
  }
  .hen { position: absolute; top: 947px; width: 108px; height: 118px; background: var(--butter); border-radius: 50% 40% 30% 45%; }
  .hen-left { left: 126px; }
  .hen-right { left: 600px; }
  .conditions {
    position: absolute; left: 0; width: 844px; top: 1094px; text-align: center;
    font-family: "Montserrat", sans-serif; font-weight: 700; font-size: 12.5px;
    line-height: 15px; letter-spacing: 1.2px; color: var(--butter);
  }
</style>
</head>
<body>
<main class="poster">
  <div class="poster-field"></div>

  <div class="price">50¢</div>
  <h1 class="headline headline-wing">WING</h1>
  <h1 class="headline headline-mondays">MONDAYS</h1>
  <p class="hours">FROM 6PM TILL LATE</p>

  <div class="wings-illustration" role="img" aria-label="Plate of chicken wings with a dipping sauce cup and lettuce"></div>

  <svg class="choice-ribbon" viewBox="0 0 580 100" aria-hidden="true">
    <polygon points="5,32 102,32 102,91 5,91 28,62" fill="#2f5f6c"/>
    <polygon points="575,32 478,32 478,91 575,91 552,62" fill="#2f5f6c"/>
    <rect x="54" y="6" width="471" height="59" fill="#2f5f6c"/>
    <polygon points="54,65 102,91 102,65" fill="#244a55"/>
    <polygon points="525,65 478,91 478,65" fill="#244a55"/>
  </svg>
  <p class="choice-label">YOUR CHOICE</p>

  <ul class="flavours">
    <li>BUFFALO SPICE WINGS</li>
    <li>HICKORY SMOKED BBQ</li>
    <li>PERI PERI</li>
  </ul>

  <div class="hen hen-left" role="img" aria-label="Decorative hen silhouette"></div>
  <div class="hen hen-right" role="img" aria-label="Decorative hen silhouette"></div>

  <p class="conditions">
    conditions apply:<br>
    minimum 4 wings per serving (of the same type)<br>
    - dine in only<br>
    - no discount apply
  </p>
</main>
</body>
</html>
```